Business Cards for new orthopaedic surgery practice

My husband and I are starting our own orthopaedic surgery practice. We are looking for a business card that is uniform, but one will have my name/title and the other will have his. You can just create one design with my name on it for now. But when I choose your design as the winning design I will ask that you add another copy with his name/title.

We are looking for classy, simple, elite all in one. We like dark blues/a little gold/yellow. Something that goes with our logo. We want our logo incorporated. Here is all the info you need:
Business name: RV Spine & Vitality Center
Location: 38915 North Bramble Ave
Willow Harbor, FL 33990
Phone: 954-218-4630
Fax: 954-571-2846
Email: info@myrvspine.example

Names: Lucinda Ferrow, M.D.
Board Certified Hand and Upper Extremity Surgeon

Emeka Dlunga, M.D.
Board Certified Hip & Knee Replacement/General Orthopaedic Surgeon

Can decide what you want to put on the back. Maybe a slogan:
Rooted in Care. Focused on You

I am just going to upload our logo. The only thing is if we select you as the winning design, the location, and phone numbers may change. We will need your help to update that once fully solidified.

Industry/Entity Type

Medical

Contact Information for Business Card

Colors
0054AA
0677BA
7BADD7
CADEEF
E8F1F8
0094D4
00A9DD
6FCCEA
C7EBF8
E9F6FB

Requirements
Must have
• class, appeal,
Should not have
• We want to air on the side of masculine if we are looking at masculine vs. feminine feel. But we still want it classy, sophisticated, and something we will love

```html
<!DOCTYPE html>
<html lang="en">
<head>
<meta charset="utf-8">
<title>Lucinda Ferrow, M.D. – Business Card</title>
<link rel="stylesheet" href="https://fonts.googleapis.com/css2?family=DM+Serif+Display&family=Inter:wght@400;500&display=swap">
<style>
  :root {
    --backdrop: #6c5c41;
    --card: #efe4d4;
    --navy: #17205a;
    --navy-soft: #1f3a6b;
    --gold: #c9a55c;
    --shadow: rgba(30, 22, 10, 0.35);
  }
  * { margin: 0; padding: 0; box-sizing: border-box; }
  html, body { width: 1200px; height: 800px; overflow: hidden; }
  body {
    background: var(--backdrop);
    position: relative;
    font-family: "Inter", Arial, sans-serif;
    color: var(--navy);
  }
  .card {
    position: absolute;
    left: 383px;
    width: 435px;
    height: 248px;
    background: var(--card);
    box-shadow: 6px 10px 24px var(--shadow);
  }
  .card--front { top: 122px; }
  .card--back { top: 430px; }

  /* Front */
  .doctor-name {
    position: absolute;
    left: 24px;
    top: 18px;
    font-family: "DM Serif Display", Georgia, serif;
    font-weight: 400;
    font-size: 44px;
    line-height: 42px;
    color: var(--navy);
    letter-spacing: -0.5px;
  }
  .credential {
    position: absolute;
    left: 24px;
    top: 109px;
    display: flex;
    align-items: center;
    gap: 6px;
    font-family: "DM Serif Display", Georgia, serif;
    font-size: 13px;
    color: var(--navy-soft);
  }
  .credential-rule {
    width: 38px;
    height: 2px;
    background: var(--gold);
  }
  .practice-mark {
    position: absolute;
    right: 22px;
    top: 26px;
    width: 110px;
    display: flex;
    flex-direction: column;
    align-items: center;
    gap: 8px;
    text-align: center;
  }
  .practice-mark-dot {
    width: 30px;
    height: 30px;
    border-radius: 50%;
    background: var(--navy);
  }
  .practice-mark-name {
    font-family: "Inter", Arial, sans-serif;
    font-weight: 500;
    font-size: 11px;
    line-height: 14px;
    color: var(--navy);
    letter-spacing: 0.6px;
    text-transform: uppercase;
  }
  .specialty {
    position: absolute;
    left: 24px;
    top: 207px;
    font-size: 13px;
    color: var(--navy);
  }
  .gold-ticks {
    position: absolute;
    left: 406px;
    top: 184px;
    display: flex;
    flex-direction: column;
    gap: 5px;
  }
  .gold-ticks span {
    display: block;
    width: 4px;
    height: 10px;
    background: var(--gold);
  }

  /* Back */
  .contact-list {
    position: absolute;
    left: 24px;
    top: 55px;
    list-style: none;
  }
  .contact-item {
    display: flex;
    align-items: flex-start;
    gap: 16px;
    font-size: 17px;
    line-height: 17px;
    color: var(--navy);
  }
  .contact-item + .contact-item { margin-top: 15px; }
  .contact-item--address + .contact-item { margin-top: 20px; }
  .contact-icon { width: 18px; height: 18px; flex: none; fill: var(--navy); }
  .practice-vertical {
    position: absolute;
    left: 395px;
    top: 29px;
    writing-mode: vertical-rl;
    font-size: 14px;
    color: var(--navy);
    white-space: nowrap;
  }
</style>
</head>
<body>

<section class="card card--front">
  <h1 class="doctor-name">Lucinda<br>Ferrow</h1>
  <div class="credential"><span>M.D.</span><span class="credential-rule"></span></div>
  <div class="practice-mark">
    <span class="practice-mark-dot"></span>
    <span class="practice-mark-name">RV Spine &amp; Vitality Center</span>
  </div>
  <p class="specialty">Board Certified Hand and Upper Extremity Surgeon</p>
  <div class="gold-ticks"><span></span><span></span><span></span></div>
</section>

<section class="card card--back">
  <ul class="contact-list">
    <li class="contact-item contact-item--address">
      <svg class="contact-icon" viewBox="0 0 24 24" aria-hidden="true"><path d="M12 1a8 8 0 0 0-8 8c0 6 8 14 8 14s8-8 8-14a8 8 0 0 0-8-8zm0 11a3 3 0 1 1 0-6 3 3 0 0 1 0 6z"/></svg>
      <span>38915 North Bramble Ave<br>Willow Harbor, FL 33990</span>
    </li>
    <li class="contact-item">
      <svg class="contact-icon" viewBox="0 0 24 24" aria-hidden="true"><path d="M6.6 10.8a15 15 0 0 0 6.6 6.6l2.2-2.2a1 1 0 0 1 1-.25 11.4 11.4 0 0 0 3.6.57 1 1 0 0 1 1 1V20a1 1 0 0 1-1 1A17 17 0 0 1 3 4a1 1 0 0 1 1-1h3.5a1 1 0 0 1 1 1c0 1.250.2 2.450.57 3.570a1 1 0 0 1-.25 1z"/></svg>
      <span>954-218-4630</span>
    </li>
    <li class="contact-item">
      <svg class="contact-icon" viewBox="0 0 24 24" aria-hidden="true"><rect x="1" y="6" width="5" height="16" rx="1.5"/><path d="M8 3h9l3 3v16H8zM10.5 12h2v2h-2zm4 0h2v2h-2zm-4 4h2v2h-2zm4 0h2v2h-2z" fill-rule="evenodd"/></svg>
      <span>954-571-2846</span>
    </li>
    <li class="contact-item">
      <svg class="contact-icon" viewBox="0 0 24 24" aria-hidden="true"><path d="M2 5h20v2l-10 6L2 7zm0 4.3 10 6 10-6V19H2z"/></svg>
      <span>info@myrvspine.example</span>
    </li>
  </ul>
  <p class="practice-vertical">RV Spine &amp; Vitality Center</p>
</section>

</body>
</html>
```